Business Card Design Project

We have a logo design and are now looking for a business card design. We supply pre-construction services to the Wireless Telecommunication Industry in the development of cell phone tower and other antenna supporting infrastructure e.g. buildings. The types of services include Real Estate Leasing, Zoning & Permitting,Surveying and A&E work. I am looking for a card that includes the logo we have selected along with the full company name. Company colors are Blue and Silver. I want something professional and that "pops". Use your imagination with the four sided star portion of the logo - it can be stretched such that it occupies a large portion of the card or kept simple the way it is. I am interested in seeing the design on a white, silver, navy, black or charcoal background or any other color you think works well with the logo. Apart from the logo that includes HRM we also need to see the full company name on the card - Harborline Relay Maintenance, Inc. The design must also show a persons name, title, address, (2) phone numbers, e-mail address and web address www.hrm.example

Target Market(s)

Cell phone carriers e.g. Quellport Mobile, BN&K, Zandex Cell, Ovalo etc.

Industry/Entity Type

Cell Phone

Requirements
Must have
• Logo and
Harborline Relay Maintenance, Inc.

```html
<!DOCTYPE html>
<html lang="en">
<head>
<meta charset="utf-8">
<title>HRM Business Card</title>
<link href="https://fonts.googleapis.com/css2?family=Open+Sans:wght@400;600&display=swap" rel="stylesheet">
<style>
  :root {
    --page-bg: #eef0f3;
    --card-white: #ffffff;
    --card-silver: #f1f3f6;
    --brand-blue: #1f8fdc;
    --brand-blue-deep: #1374bd;
    --brand-blue-light: #4fb0ee;
    --silver-text: #7d8794;
    --ink: #1c1c1c;
  }
  * { box-sizing: border-box; margin: 0; padding: 0; }
  html, body {
    width: 1200px;
    height: 900px;
    overflow: hidden;
    background: var(--page-bg);
    font-family: "Open Sans", Arial, sans-serif;
  }
  .canvas {
    width: 1200px;
    height: 900px;
    display: flex;
    align-items: center;
    justify-content: center;
  }
  .business-card {
    position: relative;
    width: 1000px;
    height: 572px;
    border-radius: 34px;
    overflow: hidden;
    background: linear-gradient(180deg, var(--card-white) 0%, var(--card-white) 55%, var(--card-silver) 100%);
    box-shadow: 0 18px 40px rgba(30, 50, 80, 0.16);
  }
  .brand-mark {
    position: absolute;
    left: 62px;
    top: 48px;
    display: flex;
    align-items: center;
    gap: 24px;
  }
  .brand-dot {
    width: 104px;
    height: 104px;
    border-radius: 50%;
    background: var(--brand-blue);
  }
  .brand-name {
    font-size: 106px;
    font-weight: 600;
    line-height: 1;
    letter-spacing: 2px;
    color: var(--brand-blue);
  }
  .company-name {
    position: absolute;
    left: 64px;
    top: 164px;
    font-size: 22px;
    font-weight: 600;
    letter-spacing: 0.5px;
    color: var(--silver-text);
  }
  .person {
    position: absolute;
    left: 48px;
    top: 222px;
  }
  .person-name {
    font-size: 31px;
    font-weight: 600;
    color: var(--brand-blue);
    line-height: 1.2;
  }
  .person-title {
    font-size: 23px;
    font-weight: 600;
    color: var(--ink);
    margin-top: 4px;
  }
  .contact-list {
    position: absolute;
    left: 46px;
    top: 336px;
    list-style: none;
  }
  .contact-item {
    display: flex;
    align-items: center;
    gap: 10px;
    font-size: 25px;
    color: var(--ink);
    height: 37px;
  }
  .contact-icon {
    width: 27px;
    height: 27px;
    flex: none;
    fill: var(--brand-blue);
  }
  .card-band {
    position: absolute;
    left: 0;
    bottom: 0;
    width: 100%;
    height: 40px;
    background: linear-gradient(180deg, var(--brand-blue-light) 0%, var(--brand-blue) 45%, var(--brand-blue-deep) 100%);
  }
</style>
</head>
<body>
<main class="canvas">
  <section class="business-card" aria-label="HRM business card">
    <div class="brand-mark">
      <span class="brand-dot" aria-hidden="true"></span>
      <span class="brand-name">HRM</span>
    </div>
    <p class="company-name">Harborline Relay Maintenance, Inc.</p>

    <div class="person">
      <p class="person-name">Dorian Vale</p>
      <p class="person-title">Manager</p>
    </div>

    <ul class="contact-list">
      <li class="contact-item">
        <svg class="contact-icon" viewBox="0 0 24 24" aria-hidden="true"><path d="M6.6 10.8c1.4 2.8 3.8 5.1 6.6 6.6l2.2-2.2c.3-.3.7-.4 1-.2 1.1.4 2.3.6 3.6.6.6 0 1 .4 1 1V20c0 .6-.4 1-1 1C10.6 21 3 13.4 3 4c0-.6.4-1 1-1h3.5c.6 0 1 .4 1 1 0 1.3.2 2.5.6 3.6.1.3 0 .7-.2 1z"/></svg>
        <span>158.555.0142</span>
      </li>
      <li class="contact-item">
        <svg class="contact-icon" viewBox="0 0 24 24" aria-hidden="true"><path d="M6.6 10.8c1.4 2.8 3.8 5.1 6.6 6.6l2.2-2.2c.3-.3.7-.4 1-.2 1.1.4 2.3.6 3.6.6.6 0 1 .4 1 1V20c0 .6-.4 1-1 1C10.6 21 3 13.4 3 4c0-.6.4-1 1-1h3.5c.6 0 1 .4 1 1 0 1.3.2 2.5.6 3.6.1.3 0 .7-.2 1z"/></svg>
        <span>713.555.0187</span>
      </li>
      <li class="contact-item">
        <svg class="contact-icon" viewBox="0 0 24 24" aria-hidden="true"><path d="M2 6a2 2 0 0 1 2-2h16a2 2 0 0 1 2 2v12a2 2 0 0 1-2 2H4a2 2 0 0 1-2-2zm2.4 0L12 11.6 19.6 6zM4 8.2V18h16V8.2l-8 5.8z"/></svg>
        <span>dorian@relaymail.example</span>
      </li>
      <li class="contact-item">
        <svg class="contact-icon" viewBox="0 0 24 24" aria-hidden="true"><path d="M12 2.5 1.5 11.5h3V21h6v-6h3v6h6v-9.5h3z"/></svg>
        <span>4820 Cedar Row, Larkfield, TX 77001</span>
      </li>
      <li class="contact-item">
        <svg class="contact-icon" viewBox="0 0 24 24" aria-hidden="true"><path d="M12 2a10 10 0 1 0 0 20 10 10 0 0 0 0-20zm6.9 9h-3a15 15 0 0 0-1.3-5.6A8 8 0 0 1 18.9 11zM12 4.1c.9 1.2 1.8 3.6 1.9 6.9h-3.8c.1-3.3 1-5.7 1.9-6.9zM9.4 5.4A15 15 0 0 0 8.1 11h-3a8 8 0 0 1 4.3-5.6zM5.1 13h3a15 15 0 0 0 1.3 5.6A8 8 0 0 1 5.1 13zm6.9 6.9c-.9-1.2-1.8-3.6-1.9-6.9h3.8c-.1 3.3-1 5.7-1.9 6.9zm2.6-1.3a15 15 0 0 0 1.3-5.6h3a8 8 0 0 1-4.3 5.6z"/></svg>
        <span>www.hrm.example</span>
      </li>
    </ul>

    <div class="card-band" aria-hidden="true"></div>
  </section>
</main>
</body>
</html>
```